Professional Package for CPA Firm

We would like a stationery design for our new CPA Firm based in Atlanta, GA called 'Vale 8'. We work with investors to help grow investments, tax free. We would like the design to have a professional/minimal look with a 'wow' factor. We need 9.5″ x 4.125″, 9x12, and 10x13 mailing envelopes, business cards, and a letterhead. We have a logo that is already complete. For the letterhead, we would like to have space to put credentials at the bottom of the page

Industry/Entity Type

CPA, Accounting

```html
<!DOCTYPE html>
<html lang="en">
<head>
<meta charset="utf-8">
<title>Vale 8 Stationery Set</title>
<link rel="stylesheet" href="https://fonts.googleapis.com/css2?family=Open+Sans:wght@400;600;700&display=swap">
<style>
:root{
  --stage:#959595;
  --paper:#ffffff;
  --navy:#0a2a40;
  --teal:#1aa3b2;
  --coral:#f2545b;
  --ink:#3a4550;
  --muted:#6b7680;
  --sig:#9fb7d8;
}
*{box-sizing:border-box;margin:0;padding:0}
html,body{width:1200px;height:680px;overflow:hidden}
body{background:var(--stage);font-family:"Open Sans",Arial,sans-serif;color:var(--ink);position:relative}
.piece{position:absolute;background:var(--paper)}
.label{position:absolute;font-size:11px;font-weight:700;color:#111;text-align:center;width:200px}
.mark{display:flex;align-items:center;gap:.25em;font-weight:700;color:var(--navy);line-height:1;letter-spacing:.02em}
.mark .dot{width:.45em;height:.45em;border-radius:50%;background:var(--coral)}
.tagline{color:var(--navy);letter-spacing:.08em;line-height:1}
.icon{width:1em;height:1em;fill:var(--navy);vertical-align:-.12em;margin-right:.4em}
.contact p{white-space:nowrap}

/* letterhead */
.letterhead{left:48px;top:32px;width:410px;height:580px}
.letterhead .brand{position:absolute;left:37px;top:62px}
.letterhead .brand .mark{font-size:21px}
.letterhead .brand .tagline{font-size:5.4px;margin-top:4px}
.letterhead .contact{position:absolute;left:274px;top:34px;border-left:1px solid #999;padding-left:8px;font-size:7.6px;line-height:10.3px;color:var(--ink)}
.letterhead .salute{position:absolute;left:37px;top:168px;font-size:10px}
.letterhead .body{position:absolute;left:37px;top:193px;width:341px;font-size:5.6px;line-height:8.8px;color:var(--muted)}
.letterhead .body p{margin-bottom:9px;text-align:justify}
.letterhead .closing{position:absolute;left:37px;top:379px;font-size:5.6px;color:var(--muted)}
.letterhead .signature{position:absolute;left:34px;top:402px;width:76px;height:30px;border-radius:6px;background:linear-gradient(90deg,var(--sig),#c9d7ea)}

/* envelope */
.env-back{left:490px;top:48px;width:355px;height:160px}
.env-back .flap{position:absolute;left:0;top:0;width:355px;height:60px}
.env-back .flap-mark{position:absolute;left:156px;top:18px;width:42px;height:20px;display:flex;align-items:center;justify-content:center}
.env-back .flap-mark span{width:9px;height:9px;border-radius:50%;background:#fff}
.env-front{left:543px;top:132px;width:356px;height:161px;box-shadow:0 1px 3px rgba(0,0,0,.15)}
.env-front .brand{position:absolute;left:21px;top:44px}
.env-front .brand .mark{font-size:14px}
.env-front .brand .tagline{font-size:3.8px;margin-top:3px}
.env-front .address{position:absolute;left:19px;top:68px;font-size:8px;line-height:10.5px}

/* cards */
.card-front{left:934px;top:32px;width:187px;height:107px;overflow:hidden}
.card-front .brand{position:absolute;left:19px;top:45px}
.card-front .brand .mark{font-size:12.5px}
.card-front .brand .tagline{font-size:3.4px;margin-top:2px}
.card-front svg.panel{position:absolute;left:0;top:0}
.card-front .details{position:absolute;right:14px;top:52px;text-align:right;color:#fff;font-size:3.6px;line-height:5.2px}
.card-front .details .name{color:var(--teal);font-size:5.6px;font-weight:600;line-height:6.5px}
.card-front .details .role{color:var(--teal);font-size:3.6px;margin-bottom:4px}
.card-front .details .icon{fill:var(--teal);margin:0 0 0 .4em}
.card-back{left:930px;top:177px;width:193px;height:110px;background:linear-gradient(135deg,#0b3550,#082437 60%,#0d4060)}

/* email signatures */
.sig-one{left:496px;top:335px;width:176px;height:266px}
.sig-one .brand{position:absolute;left:23px;top:66px}
.sig-one .brand .mark{font-size:21px}
.sig-one .brand .tagline{font-size:5.6px;margin-top:4px}
.sig-one .name{position:absolute;left:23px;top:110px;font-size:16px;font-weight:600;color:var(--navy)}
.sig-one .role{position:absolute;left:23px;top:133px;font-size:11px;color:var(--teal)}
.sig-one .address{position:absolute;left:23px;top:150px;font-size:11px;line-height:14px}
.sig-one .contact{position:absolute;left:23px;top:187px;font-size:11px;line-height:14.4px}

.sig-two{left:699px;top:335px;width:455px;height:141px}
.sig-two .brand{position:absolute;left:103px;top:67px}
.sig-two .brand .mark{font-size:21px}
.sig-two .brand .tagline{font-size:5.8px;margin-top:4px}
.sig-two .contact{position:absolute;left:206px;top:35px;border-left:1px solid #333;padding-left:22px;font-size:11px;line-height:14.3px}

.sig-three{left:695px;top:513px;width:455px;height:87px}
.sig-three .brand{position:absolute;left:44px;top:30px}
.sig-three .brand .mark{font-size:15px}
.sig-three .brand .tagline{font-size:4px;margin-top:3px}
.sig-three .col{position:absolute;top:19px;height:52px;border-left:1px solid #333;font-size:11px;line-height:14px;padding-left:26px;padding-top:3px}
.sig-three .col.addr{left:128px}
.sig-three .col.reach{left:286px;padding-left:25px}
</style>
</head>
<body>

<svg width="0" height="0" style="position:absolute" aria-hidden="true">
  <symbol id="i-phone" viewBox="0 0 24 24"><path d="M6.6 10.8a15 15 0 0 0 6.6 6.6l2.2-2.2a1 1 0 0 1 1-.25 11.4 11.4 0 0 0 3.6.57 1 1 0 0 1 1 1V20a1 1 0 0 1-1 1A17 17 0 0 1 3 4a1 1 0 0 1 1-1h3.5a1 1 0 0 1 1 1c0 1.25.2 2.45.57 3.57a1 1 0 0 1-.25 1z"/></symbol>
  <symbol id="i-mobile" viewBox="0 0 24 24"><path d="M7 2h10a1 1 0 0 1 1 1v18a1 1 0 0 1-1 1H7a1 1 0 0 1-1-1V3a1 1 0 0 1 1-1zm1 3v13h8V5z"/></symbol>
  <symbol id="i-mail" viewBox="0 0 24 24"><path d="M2 5h20v14H2zm2 2v.5l8 5 8-5V7zm0 3v7h16v-7l-8 5z"/></symbol>
  <symbol id="i-globe" viewBox="0 0 24 24"><path d="M12 2a10 10 0 1 0 0 20 10 10 0 0 0 0-20zm-1 17.9A8 8 0 0 1 4.2 10l4.8 4.8v1a2 2 0 0 0 2 2zm6.9-2.5a2 2 0 0 0-1.9-1.4h-1v-3a1 1 0 0 0-1-1H8v-2h2a1 1 0 0 0 1-1V7h2a2 2 0 0 0 2-2v-.4a8 8 0 0 1 2.9 12.8z"/></symbol>
</svg>

<!-- Letterhead -->
<section class="piece letterhead">
  <div class="brand">
    <div class="mark">Vale 8<span class="dot"></span></div>
    <div class="tagline">CPAs and Tax Advisors</div>
  </div>
  <div class="contact">
    <p>2214 Birchwood Lane</p>
    <p>Harlow, Georgia 30421</p>
    <p><svg class="icon"><use href="#i-phone"/></svg>555-214-7730</p>
    <p><svg class="icon"><use href="#i-mobile"/></svg>555-318-6042</p>
    <p><svg class="icon"><use href="#i-mail"/></svg>info@vale8.com</p>
    <p><svg class="icon"><use href="#i-globe"/></svg>www.vale8.com</p>
  </div>
  <p class="salute">Dear Mr. Reyes,</p>
  <div class="body">
    <p>Lorem ipsum dolor sit amet, consectetur adipiscing elit. Donec orci purus, luctus vitae dignissim eu, iaculis sed purus. Vivamus faucibus, ipsum nec aliquet viverra, leo mauris condimentum ligula, sit amet sagittis enim ligula quis arcu. Nam egestas tortor id nisi porttitor mattis. In tortor ante, ultricies in suscipit a, tempus non massa. Vivamus et auctor mi. Fusce vel massa nulla. Phasellus nec eros mauris, et scelerisque orci.</p>
    <p>Donec malesuada orci vitae nulla accumsan porta a id massa. Quisque accumsan iaculis magna sit amet fringilla. Maecenas consequat, magna eget tincidunt semper, odio nibh rutrum mi, id feugiat ante nisi eu risus. Vestibulum nunc orci, rhoncus a placerat in, ultricies in mi. Cras mattis varius eros, vel fringilla nisi suscipit eget. Quisque scelerisque sagittis nulla at porttitor.</p>
    <p>Sed id augue vitae urna euismod commodo aliquet a quam. Pellentesque arcu velit, cursus et malesuada ut, consequat et diam. Nullam erat sem, rhoncus id ullamcorper vitae, rhoncus et arcu. In ultricies ultricies nulla, ut rutrum nisi iaculis at. Donec eu magna a metus ornare faucibus. Fusce aliquet faucibus ultricies. Morbi semper, est id tincidunt gravida, sem arcu adipiscing lacus, ac bibendum nulla leo eu purus. Quisque nec diam sed risus consectetur a cumsan quis quis nibh. Vestibulum id purus lorem.</p>
    <p>It is a long established fact that a reader will be distracted by the readable content of a page when looking at its layout. The point of using Lorem Ipsum is that it has a more-or-less normal distribution of letters, as opposed to using 'Content here, content here', making it look like readable English. Many desktop publishing packages</p>
  </div>
  <p class="closing">Sincerely,</p>
  <div class="signature" role="img" aria-label="Handwritten signature of Daniel Reyes"></div>
</section>
<p class="label" style="left:138px;top:617px">Letterhead</p>

<!-- Envelope -->
<section class="piece env-back">
  <svg class="flap" viewBox="0 0 355 60" aria-hidden="true">
    <path d="M0 0H355L349 24Q344 59 318 59H37Q11 59 6 24Z" fill="var(--navy)"/>
  </svg>
  <div class="flap-mark"><span></span></div>
</section>
<section class="piece env-front">
  <div class="brand">
    <div class="mark">Vale 8<span class="dot"></span></div>
    <div class="tagline">CPAs and Tax Advisors</div>
  </div>
  <div class="address">
    <p>2214 Birchwood Lane</p>
    <p>Harlow, Georgia 30421</p>
  </div>
</section>
<p class="label" style="left:624px;top:299px">Envelope</p>

<!-- Business cards -->
<section class="piece card-front">
  <svg class="panel" width="187" height="107" viewBox="0 0 187 107" aria-hidden="true">
    <path d="M187 32L160 8Q151 0 142 8L86 62Q76 72 80 85L86 100Q89 107 97 107H187Z" fill="var(--navy)"/>
    <path d="M162 6L187 30" stroke="var(--teal)" stroke-width="1.5" fill="none"/>
  </svg>
  <div class="brand">
    <div class="mark">Vale 8<span class="dot"></span></div>
    <div class="tagline">CPAs and Tax Advisors</div>
  </div>
  <div class="details">
    <p class="name">DANIEL REYES</p>
    <p class="role">President</p>
    <p>2214 Birchwood Lane</p>
    <p>Harlow, Georgia 30421</p>
    <p style="margin-top:2px">555-214-7730<svg class="icon"><use href="#i-phone"/></svg></p>
    <p>555-406-2291<svg class="icon"><use href="#i-mobile"/></svg></p>
    <p>info@vale8.com<svg class="icon"><use href="#i-mail"/></svg></p>
    <p>www.vale8.com<svg class="icon"><use href="#i-globe"/></svg></p>
  </div>
</section>
<p class="label" style="left:915px;top:152px">Front Card</p>

<section class="piece card-back" role="img" aria-label="Dark navy repeating brand pattern for the card reverse"></section>
<p class="label" style="left:905px;top:302px">Back Card</p>

<!-- Email signatures -->
<section class="piece sig-one">
  <div class="brand">
    <div class="mark">Vale 8<span class="dot"></span></div>
    <div class="tagline">CPAs and Tax Advisors</div>
  </div>
  <p class="name">Daniel Reyes</p>
  <p class="role">President</p>
  <div class="address" style="top:151px">
    <p>2214 Birchwood Lane</p>
    <p>Harlow, Georgia 30421</p>
  </div>
  <div class="contact">
    <p><svg class="icon"><use href="#i-phone"/></svg>555-214-7730</p>
    <p><svg class="icon"><use href="#i-mobile"/></svg>555-318-6042</p>
    <p><svg class="icon"><use href="#i-mail"/></svg>info@vale8.com</p>
    <p><svg class="icon"><use href="#i-globe"/></svg>www.vale8.com</p>
  </div>
</section>
<p class="label" style="left:470px;top:610px">Email Signature 1</p>

<section class="piece sig-two">
  <div class="brand">
    <div class="mark">Vale 8<span class="dot"></span></div>
    <div class="tagline">CPAs and Tax Advisors</div>
  </div>
  <div class="contact">
    <p>2214 Birchwood Lane</p>
    <p>Harlow, Georgia 30421</p>
    <p><svg class="icon"><use href="#i-phone"/></svg>555-214-7730</p>
    <p><svg class="icon"><use href="#i-mail"/></svg>info@vale8.com</p>
    <p><svg class="icon"><use href="#i-globe"/></svg>www.vale8.org</p>
  </div>
</section>
<p class="label" style="left:803px;top:483px">Email Signature 2</p>

<section class="piece sig-three">
  <div class="brand">
    <div class="mark">Vale 8<span class="dot"></span></div>
    <div class="tagline">CPAs and Tax Advisors</div>
  </div>
  <div class="col addr">
    <p>2214 Birchwood Lane</p>
    <p>Harlow,</p>
    <p>Georgia 30421</p>
  </div>
  <div class="col reach contact">
    <p><svg class="icon"><use href="#i-phone"/></svg>555-214-7730</p>
    <p><svg class="icon"><use href="#i-mail"/></svg>info@vale8.com</p>
    <p><svg class="icon"><use href="#i-globe"/></svg>www.vale8.com</p>
  </div>
</section>
<p class="label" style="left:816px;top:608px">Email Signature 3</p>

</body>
</html>
```